A Weather Forecasting Site needs designs

We need a website design for our new venture which is a weather forecasting website. This website should have the latest design trends.

Menu
Weather, Maps, Videos and Photos

The home page requirements are as follows:
- Search Bar
- Local Weather
- Weather forecast of major cities in the World
Favorite locations
- Space for ADs
- Email signup

Weather Details page
This page will be redirected from the home page when you click on any of the weather forecast section

We are open to all kinds of designs and ideas. Feel free to you colors which suite your design.

```html
<!DOCTYPE html>
<html lang="en">
<head>
<meta charset="utf-8">
<title>Skycast – America Weather</title>
<link href="https://fonts.googleapis.com/css2?family=Montserrat:wght@400;500;600;700&family=Open+Sans:wght@400;600;700&family=Oswald:wght@700&display=swap" rel="stylesheet">
<style>
:root{
  --ink:#111;
  --dark:#1b1b1b;
  --darker:#0f0f0f;
  --orange:#f08a24;
  --orange-soft:#f4a34a;
  --grey-bar:#efefef;
  --grey-line:#cfcfcf;
  --cell:#f4f4f4;
  --text:#333;
  --muted:#bdbdbd;
  --blue:#1e6fb8;
  --white:#fff;
}
*{box-sizing:border-box;margin:0;padding:0}
html,body{width:1200px;height:2347px;overflow:hidden}
body{position:relative;background:var(--white);font-family:"Open Sans",Arial,sans-serif;color:var(--text)}
.abs{position:absolute}

/* top utility bar */
.utility{left:0;top:0;width:1200px;height:25px;background:var(--ink);color:#ddd;font-size:10px;display:flex;align-items:center;padding-left:56px;gap:22px}
.utility .crumbs span{margin:0 6px;color:#888}
.utility .sep{width:1px;height:14px;background:#555}
.search{left:945px;top:0;width:166px;height:25px;background:var(--white);font-size:9px;color:#999;padding:7px 8px}
.search-btn{left:1111px;top:0;width:33px;height:25px;background:var(--orange)}

/* header */
.brand{left:55px;top:53px;display:flex;align-items:center;gap:8px;font-family:"Oswald",sans-serif;font-weight:700;font-size:46px;line-height:1;color:#2b2b2b;letter-spacing:1px}
.brand-mark{width:14px;height:14px;background:var(--orange)}
.promo{left:500px;top:41px;width:644px;height:84px;background:linear-gradient(90deg,#d8d8d8 0,#8a2a3a 22%,#6e1f30 100%);color:var(--white)}
.promo-copy{left:150px;top:12px;font-family:"Montserrat",sans-serif}
.promo-copy .l1{font-size:22px;font-weight:700;display:flex;align-items:center;gap:8px}
.promo-copy .l1 small{font-size:8px;font-weight:400;line-height:1.2;width:120px}
.promo-copy .l2{font-size:22px;font-weight:700;color:var(--orange-soft)}
.promo-copy .l2 span{color:var(--white)}
.promo-btn{left:505px;top:26px;width:118px;height:32px;background:var(--orange);font-family:"Montserrat",sans-serif;font-size:11px;font-weight:600;text-align:center;line-height:32px}

/* nav */
.nav{left:0;top:141px;width:1200px;height:40px;background:var(--ink)}
.nav ul{list-style:none;display:flex;height:40px;margin-left:55px;font-family:"Montserrat",sans-serif;font-size:13px;color:#eee}
.nav li{display:flex;align-items:center;justify-content:center;border-right:1px solid #444}
.nav li.now{background:#444;width:152px}
.nav li.w1{width:154px}.nav li.w2{width:133px}.nav li.w3{width:133px}.nav li.w4{width:102px}
.watch{left:970px;top:141px;width:174px;height:40px;background:var(--orange);font-family:"Montserrat",sans-serif;font-size:13px;color:var(--white);display:flex;align-items:center;justify-content:center;gap:10px}

/* local strip */
.localbar{left:0;top:181px;width:1200px;height:69px;background:var(--grey-bar);font-family:"Montserrat",sans-serif;font-size:13px;color:#444}
.localbar .chip{position:absolute;top:11px;width:50px;height:50px;border-radius:50%;background:var(--white);display:flex;align-items:center;justify-content:center}
.localbar .lbl{position:absolute;top:26px;font-weight:500}

/* conditions */
.section-title{left:0;width:1200px;top:280px;text-align:center;font-family:"Montserrat",sans-serif;font-weight:600;font-size:28px;color:var(--ink)}
.conditions{left:52px;top:346px;width:1093px;border:2px solid var(--grey-line);display:grid;grid-template-columns:1fr 1fr;background:var(--cell)}
.conditions .place{height:81px;border-bottom:2px solid var(--grey-line);display:flex;align-items:center;padding:0 28px;font-size:24px;color:#444;position:relative;background:linear-gradient(#fafafa,#ececec)}
.conditions .place:nth-child(odd){border-right:2px solid var(--grey-line)}
.conditions .place:nth-last-child(-n+2){border-bottom:none}
.conditions .place svg{position:absolute;left:359px;top:17px}
.conditions .temp{position:absolute;left:456px;top:30px;font-size:22px}

/* hero video */
.hero{left:52px;top:784px;width:710px;height:368px;background:radial-gradient(ellipse at 45% 30%,#6f7d6a 0,#34402f 45%,#141a12 100%)}
.now-card{left:30px;top:73px;width:148px;height:88px;background:var(--white);font-size:11px;color:#333;padding:5px 8px;line-height:1.2}
.now-card small{font-size:8px;display:block;color:#666}
.now-card .big{display:flex;align-items:center;gap:8px;font-size:32px;margin-top:4px}
.now-card .big i{width:24px;height:24px;border-radius:50%;background:#f5c02a;display:block}
.now-card .big sup{font-size:9px}
.tab{top:138px;height:19px;background:var(--orange);color:var(--white);font-size:8px;font-weight:700;padding:0 6px;line-height:19px;white-space:nowrap}

/* sidebar */
.follow{left:803px;top:810px;font-family:"Montserrat",sans-serif;font-size:20px;color:var(--ink)}
.follow-rule{left:803px;top:856px;width:341px;height:4px;background:#222}
.follow-tip{left:828px;top:860px;width:0;height:0;border-left:6px solid transparent;border-right:6px solid transparent;border-top:7px solid #222}
.socials{left:806px;top:878px;display:flex;gap:6px}
.socials i{width:33px;height:33px;display:block}
.tile-map{left:803px;top:939px;width:341px;height:220px;background:linear-gradient(135deg,#6e9fa8,#9b8a5f 50%,#5d8aa0);display:flex;align-items:center;justify-content:center;text-align:center;font-family:"Montserrat",sans-serif;font-weight:700;font-size:23px;color:var(--white);line-height:1.55}

/* cards */
.card-title{height:47px;background:var(--ink);color:var(--white);font-family:"Montserrat",sans-serif;font-weight:600;font-size:21px;padding:9px 0 0 38px}
.card-media{position:absolute;top:47px;left:0;right:0;bottom:0}
.card-foot{position:absolute;left:0;right:0;bottom:0;height:44px;background:rgba(255,255,255,.75);font-size:16px;color:#333;padding:11px 0 0 20px}
.video-card{left:52px;top:1189px;width:327px;height:286px}
.video-card .card-media{background:linear-gradient(90deg,#3b3f4a 0,#5c6f8a 40%,#8fa6c8 100%)}
.video-card .badge{position:absolute;left:0;bottom:0;width:51px;height:44px;background:var(--orange)}
.video-card .card-foot{left:51px;padding-left:18px}
.sat-card{left:435px;top:1189px;width:327px;height:286px}
.sat-card .card-title{padding-left:22px}
.sat-card .card-media{background:linear-gradient(160deg,#1d3f7a,#2f6f8a 45%,#5c7c4a 75%,#2a4f8c)}

.portal{left:803px;top:1197px;width:341px;height:383px;border:2px solid #555;padding:30px 0 0 30px}
.portal h3{font-family:"Open Sans",sans-serif;font-size:28px;font-weight:600;color:var(--blue);letter-spacing:-.5px}
.portal .rule{width:275px;height:2px;background:#999;margin:2px 0 6px}
.portal h4{font-size:23px;font-weight:400;color:#222}
.portal p{font-size:15px;line-height:1.3;color:#222;width:270px;margin-top:6px}
.portal .more{position:absolute;left:243px;top:173px;color:#e4552a;font-size:14px}
.portal .sat{position:absolute;left:16px;top:241px;width:300px;height:120px;background:radial-gradient(circle at 62% 50%,#e8ecef 0,#9fb0bd 18%,#2d5380 45%,#1c3452 100%)}

.map-block{left:52px;top:1515px;width:710px;height:414px}
.map-block .card-title{height:45px;padding-left:38px;padding-top:8px}
.map-block .card-media{top:45px;background:linear-gradient(180deg,#1d3f86 0,#56704a 30%,#8a7a54 60%,#3f6a3a 85%,#1e4b95 100%)}

.ad{left:803px;top:1623px;width:341px;height:306px;background:radial-gradient(ellipse at 50% 40%,#555 0,#222 60%,#111 100%)}
.ad-panel{left:52px;top:56px;width:225px;height:230px;background:rgba(140,140,140,.55);text-align:center;color:var(--white)}
.ad-panel .s{font-size:16px;line-height:1.15;margin-top:28px}
.ad-panel .a{font-family:"Oswald",sans-serif;font-size:36px;line-height:1.05;margin-top:6px}
.ad-panel .h{font-family:"Oswald",sans-serif;font-size:36px;line-height:1;color:var(--orange-soft)}
.ad-panel .stars{font-size:22px;letter-spacing:4px;margin-top:6px}
.ad-panel .stars b{color:#f5b82a;font-weight:400}

/* footer */
.footer{left:0;top:1959px;width:1200px;height:310px;background:var(--dark);color:#ddd}
.footer .col{position:absolute;top:35px}
.footer h5{font-family:"Montserrat",sans-serif;font-weight:500;font-size:18px;color:var(--white);margin-bottom:22px}
.footer ul{list-style:none;font-size:14px;line-height:31px}
.footer-bottom{left:0;top:2269px;width:1200px;height:78px;background:var(--darker);color:#ddd;font-size:13px;padding:33px 0 0 58px}
.footer-dots{left:1008px;top:2295px;display:flex;gap:8px}
.footer-dots i{width:18px;height:18px;border-radius:50%;display:block}
</style>
</head>
<body>
<svg width="0" height="0" style="position:absolute">
  <symbol id="sun-cloud" viewBox="0 0 56 48">
    <g fill="none" stroke="#f08a24" stroke-width="2" stroke-linecap="round">
      <circle cx="22" cy="20" r="9"/>
      <line x1="22" y1="2" x2="22" y2="6"/><line x1="8" y1="8" x2="11" y2="11"/><line x1="4" y1="20" x2="8" y2="20"/>
      <line x1="36" y1="8" x2="33" y2="11"/><line x1="8" y1="32" x2="11" y2="29"/>
      <path d="M20 42h26a7 7 0 0 0 0-14 10 10 0 0 0-19-2 8 8 0 0 0-7 16z" fill="#fff" stroke="#bbb"/>
    </g>
  </symbol>
</svg>

<!-- utility bar -->
<div class="abs utility">
  <div>◯ ENGLISH (US), °C</div>
  <div class="crumbs">▾ World<span>›</span>America<span>›</span>Lorem<span>›</span>Epsam</div>
  <div class="sep"></div>
  <div>● Singup</div>
</div>
<div class="abs search">Search...</div>
<div class="abs search-btn">
  <svg width="33" height="25" viewBox="0 0 33 25"><circle cx="15" cy="11" r="5" fill="none" stroke="#fff" stroke-width="2"/><line x1="19" y1="15" x2="22" y2="18" stroke="#fff" stroke-width="2"/></svg>
</div>

<!-- header -->
<div class="abs brand">SKYCAST<span class="brand-mark"></span></div>
<div class="abs promo">
  <div class="abs promo-copy">
    <div class="l1">ASK THE <small>An Amazingly Fresh News/Magazine Theme for SitePress</small></div>
    <div class="l2">USERS ABOUT BREEZE <span>News?</span></div>
  </div>
  <div class="abs promo-btn">BUY NOW</div>
</div>

<!-- nav -->
<nav class="abs nav">
  <ul>
    <li class="now">Now 1:07 pm IST</li>
    <li class="w1">Weekend</li>
    <li class="w2">Extended</li>
    <li class="w3">Month</li>
    <li class="w4">Satellite</li>
  </ul>
</nav>
<div class="abs watch">Watch Videos
  <svg width="12" height="12" viewBox="0 0 12 12"><circle cx="6" cy="6" r="5" fill="none" stroke="#fff"/><path d="M5 4l3 2-3 2z" fill="#fff"/></svg>
</div>

<!-- local strip -->
<div class="abs localbar">
  <div class="chip" style="left:80px"><svg width="30" height="26"><use href="#sun-cloud"/></svg></div>
  <div class="lbl" style="left:160px">America Weather</div>
  <div class="chip" style="left:332px"><svg width="30" height="26"><use href="#sun-cloud"/></svg></div>
  <div class="lbl" style="left:426px">New York , America &nbsp;&nbsp;Local Weather36˚C</div>
  <div class="chip" style="left:770px">
    <svg width="22" height="22" viewBox="0 0 22 22" stroke="#4a78c2" stroke-width="1.6"><line x1="11" y1="2" x2="11" y2="20"/><line x1="3" y1="6.5" x2="19" y2="15.5"/><line x1="3" y1="15.5" x2="19" y2="6.5"/></svg>
  </div>
  <div class="lbl" style="left:855px">Personalized Forecasts: &nbsp;&nbsp;&nbsp;&nbsp;Allergies</div>
</div>

<!-- conditions -->
<h1 class="abs section-title">America Weather Conditions - Nearby Places division</h1>
<div class="abs conditions">
  <div class="place">Haora<svg width="56" height="48"><use href="#sun-cloud"/></svg><span class="temp">33˚</span></div>
  <div class="place">Atghara<svg width="56" height="48"><use href="#sun-cloud"/></svg><span class="temp">33˚</span></div>
  <div class="place">Chak Kolarkhal<svg width="56" height="48"><use href="#sun-cloud"/></svg><span class="temp">33˚</span></div>
  <div class="place">Mukundapur<svg width="56" height="48"><use href="#sun-cloud"/></svg><span class="temp">33˚</span></div>
  <div class="place">Karimpur<svg width="56" height="48"><use href="#sun-cloud"/></svg><span class="temp">33˚</span></div>
  <div class="place">Haridevpur<svg width="56" height="48"><use href="#sun-cloud"/></svg><span class="temp">33˚</span></div>
  <div class="place">Bhagabanpur<svg width="56" height="48"><use href="#sun-cloud"/></svg><span class="temp">33˚</span></div>
  <div class="place">Krishnanagar<svg width="56" height="48"><use href="#sun-cloud"/></svg><span class="temp">33˚</span></div>
  <div class="place">Jagatipata<svg width="56" height="48"><use href="#sun-cloud"/></svg><span class="temp">33˚</span></div>
  <div class="place">Ramkantapur<svg width="56" height="48"><use href="#sun-cloud"/></svg><span class="temp">33˚</span></div>
</div>

<!-- hero video -->
<div class="abs hero" role="img" aria-label="Video still of a misty forest with a hooded figure among the trees">
  <div class="abs now-card">Washington, DC, USA<small>Monday 7:00 AM</small><small>Sunny</small>
    <div class="big"><i></i>12<sup>°C|°F</sup></div>
  </div>
  <div class="abs tab" style="left:226px">CURRENT WEATHER</div>
  <div class="abs tab" style="left:349px">TODAY May 15</div>
  <div class="abs tab" style="left:467px">TONIGHT May 15</div>
  <div class="abs tab" style="left:586px">TOMORROW May 16</div>
</div>

<!-- sidebar -->
<div class="abs follow">Follow us</div>
<div class="abs follow-rule"></div>
<div class="abs follow-tip"></div>
<div class="abs socials">
  <i style="background:#f08a24"></i><i style="background:#2b7bbd"></i><i style="background:#e43b3b"></i><i style="background:#5fa8d8"></i><i style="background:#3b5fa8"></i><i style="background:#35a3e8"></i>
</div>
<div class="abs tile-map" role="img" aria-label="World map background">VIEW STELIGHT<br>MAP</div>

<!-- cards -->
<div class="abs video-card">
  <div class="card-title">Video Weather Forecast</div>
  <div class="card-media" role="img" aria-label="Presenter in front of a regional weather map"></div>
  <div class="badge"></div>
  <div class="card-foot">America Weather</div>
</div>
<div class="abs sat-card">
  <div class="card-title">America Weather Satellite</div>
  <div class="card-media" role="img" aria-label="Satellite view of the Americas with cloud cover"></div>
  <div class="card-foot">See Weather Satellite</div>
</div>

<div class="abs portal">
  <h3>Weather Data Portal</h3>
  <div class="rule"></div>
  <h4>ClimaCore in XML</h4>
  <p>ClimaCore Global is the simplest way to get ClimaCore's Weather Data at your end, starting at US$ 0.69/month</p>
  <span class="more">more›</span>
  <div class="sat" role="img" aria-label="Satellite image of a hurricane over the ocean"></div>
</div>

<div class="abs map-block">
  <div class="card-title">America Weather Map - Nearby Places</div>
  <div class="card-media" role="img" aria-label="Weather map of North America with city forecasts"></div>
</div>

<div class="abs ad" role="img" aria-label="Advertising space with dark photo background">
  <div class="abs ad-panel">
    <div class="s">Best Solution<br>for Your Business</div>
    <div class="a">ADVERTISE</div>
    <div class="h">HERE</div>
    <div class="stars"><b>★★★</b>★★</div>
  </div>
</div>

<!-- footer -->
<footer class="abs footer">
  <div class="col" style="left:56px">
    <h5>COMPANY</h5>
    <ul><li>Superior Accuracy in Action</li><li>About Skycast</li><li>Media Kit</li><li>Careers</li><li>Press</li><li>Contact Us</li></ul>
  </div>
  <div class="col" style="left:490px">
    <h5>PRODUCTS &amp; SERVICES</h5>
    <ul style="line-height:27.5px"><li>Enterprise Solutions</li><li>Delta Data Analytics</li><li>Weather Network</li><li>StoryTeller</li><li>Tools for Broadcast</li><li>Radio &amp; Newspaper</li><li>Weather APIs</li></ul>
  </div>
  <div class="col" style="left:918px">
    <h5>APPS &amp; DOWNLOADS</h5>
    <ul><li>Phone App</li><li>Tablet App</li><li>Desktop App</li><li>See all Apps &amp; Downloads</li></ul>
  </div>
</footer>
<div class="abs footer-bottom">© 2017 Skycast, Inc. All Rights Reserved.</div>
<div class="abs footer-dots">
  <i style="background:#3b5fa8"></i><i style="background:#35a3e8"></i><i style="background:#e4553a"></i><i style="background:#2b7bbd"></i><i style="background:#d9333f"></i>
</div>
</body>
</html>
```